Need a new letterhead

Need a new fresh exciting letterhead. Remove the footer...info is outdated.

Target Market(s)

B2B

Industry/Entity Type

Electrical Power

Colors

Designer to choose colors to be used in the design.

Requirements
Must have
• Red and Blue Corvane Systems Logo
Nice to have
• Lighting the way to sustainability in footer...reorganize the words?

```html
<!DOCTYPE html>
<html lang="en">
<head>
<meta charset="utf-8">
<title>Corvane Systems Letterhead</title>
<link rel="stylesheet" href="https://fonts.googleapis.com/css2?family=Figtree:wght@400;500;600;800&display=swap">
<style>
  :root {
    --brand-red: #e3202b;
    --brand-blue: #263580;
    --ink: #1b1b1b;
    --link-blue: #2a74c4;
    --paper: #ffffff;
  }
  * { margin: 0; padding: 0; box-sizing: border-box; }
  html, body { width: 927px; height: 1200px; overflow: hidden; background: var(--paper); }
  body { font-family: "Figtree", sans-serif; color: var(--ink); }
  .letterhead { position: relative; width: 927px; height: 1200px; background: var(--paper); }

  .brand-name {
    position: absolute; left: 74px; top: 78px;
    font-weight: 800; font-size: 46px; line-height: 50px;
    color: var(--brand-red); letter-spacing: -0.5px;
  }

  .contact {
    position: absolute; right: 76px; top: 60px;
    text-align: right; font-size: 16.5px; line-height: 22px;
  }
  .contact .phones { margin-top: 8px; }
  .contact .web { display: inline-block; margin-top: 8px; color: var(--link-blue); text-decoration: underline; }

  .rule { position: absolute; left: 0; width: 100%; height: 1.5px; }
  .rule.red { background: var(--brand-red); }
  .rule.blue { background: var(--brand-blue); }

  .letter { position: absolute; left: 134px; top: 0; width: 658px; font-size: 17.5px; }
  .letter .field { position: absolute; left: 0; white-space: nowrap; }
  .letter .body { position: absolute; left: 0; top: 427px; width: 658px; font-size: 19px; }
  .letter .body p { text-align: justify; line-height: 22.6px; margin-bottom: 30px; }

  .tagline {
    position: absolute; left: 0; top: 1094px; width: 100%;
    text-align: center; font-size: 18px; font-weight: 600;
    letter-spacing: 1.5px; color: var(--brand-blue); white-space: nowrap;
  }
  .tagline .accent { color: var(--brand-red); }

  .footer-band {
    position: absolute; left: 0; top: 1146px; width: 100%; height: 54px;
    background: var(--brand-blue); color: #fff;
    display: flex; align-items: center; justify-content: center;
    font-size: 19px; letter-spacing: 4.2px; font-weight: 500;
  }
</style>
</head>
<body>
<div class="letterhead">
  <div class="brand-name">Corvane<br>Systems</div>

  <div class="contact">
    <div>417 Halden Street</div>
    <div>Arnover, Maryland 21407</div>
    <div class="phones">
      <div>Phone: 555-014-2260</div>
      <div>Fax: 555-014-2261</div>
    </div>
    <span class="web">www.CorvaneSystems.com</span>
  </div>

  <div class="rule red" style="top:197px"></div>
  <div class="rule blue" style="top:200px"></div>

  <div class="letter">
    <div class="field" style="top:263px">SENT VIA EMAIL:</div>
    <div class="field" style="top:345px">RE:</div>
    <div class="body">
      <p>“Lorem ipsum dolor sit amet, consectetur adipiscing elit, sed do eiusmod tempor incididunt ut labore et dolore magna aliqua. Ut enim ad minim veniam, quis nostrud exercitation ullamco laboris nisi ut aliquip ex ea commodo consequat. Duis aute irure dolor in reprehenderit in voluptate velit esse cillum dolore eu fugiat nulla pariatur. Excepteur sint occaecat cupidatat non proident, sunt in culpa qui officia deserunt mollit anim id est laborum.”</p>
      <p>“Lorem ipsum dolor sit amet, consectetur adipiscing elit, sed do eiusmod tempor incididunt ut labore et dolore magna aliqua. Ut enim ad minim veniam, quis nostrud exercitation ullamco laboris nisi ut aliquip ex ea commodo consequat. Duis aute irure dolor in reprehenderit in voluptate velit esse cillum dolore eu fugiat nulla pariatur. Excepteur sint occaecat cupidatat non proident, sunt in culpa qui officia deserunt mollit anim id est laborum.”</p>
      <p>“Lorem ipsum dolor sit amet, consectetur adipiscing elit, sed do eiusmod tempor incididunt ut labore et dolore magna aliqua. Ut enim ad minim veniam, quis nostrud exercitation ullamco laboris nisi ut aliquip ex ea commodo consequat. Duis aute irure dolor in reprehenderit in voluptate velit esse cillum dolore eu fugiat nulla pariatur. Excepteur sint occaecat cupidatat non proident, sunt in culpa qui officia deserunt mollit anim id est laborum.”</p>
    </div>
  </div>

  <div class="tagline">Lighting the way to <span class="accent">sustainability</span></div>

  <div class="rule red" style="top:1142px"></div>
  <div class="footer-band">www.CorvaneSystems.com</div>
</div>
</body>
</html>
```